DELVANE ROOFING YARD SIGN

We need a yard sign to put in our customers' yards when we are roofing their home.
Delvane Roofing
468 Pettigrew Rd
Lake Charles LA 70452
phone: 337-555-0148

Maybe some verbiage like "Your Hometown Roofing Experts"
or
"Family Owned Since 1956"

```html
<!DOCTYPE html>
<html lang="en">
<head>
<meta charset="utf-8">
<title>Delvane Roofing Yard Sign</title>
<link rel="stylesheet" href="https://fonts.googleapis.com/css2?family=Roboto+Slab:wght@500;700;800;900&family=Roboto:wght@900&display=swap">
<style>
  :root {
    --navy: #12116b;
    --charcoal: #444446;
    --ink: #3a3a3c;
    --panel: #f0f0f1;
    --panel-edge: #e2e2e4;
    --white: #ffffff;
    --backdrop: #d9d9db;
  }
  html, body {
    margin: 0;
    width: 1200px;
    height: 1000px;
    overflow: hidden;
    background: var(--backdrop);
  }
  .yard-sign {
    position: absolute;
    left: 0;
    top: 50px;
    width: 1200px;
    height: 900px;
    background: linear-gradient(135deg, var(--white) 0%, var(--panel) 45%, var(--panel-edge) 100%);
    overflow: hidden;
  }
  .sign-shapes {
    position: absolute;
    inset: 0;
  }
  .brand-seal {
    position: absolute;
    left: 90px;
    top: 73px;
    width: 470px;
    height: 470px;
    display: flex;
    align-items: center;
    justify-content: center;
    text-align: center;
  }
  .brand-name {
    font-family: "Roboto Slab", serif;
    font-weight: 800;
    font-size: 50px;
    line-height: 1.15;
    color: var(--navy);
    letter-spacing: 1px;
  }
  .tagline-top {
    position: absolute;
    right: 52px;
    top: 48px;
    font-family: "Roboto Slab", serif;
    font-weight: 700;
    font-size: 33px;
    color: var(--white);
  }
  .headline {
    position: absolute;
    left: 648px;
    top: 152px;
    font-family: "Roboto Slab", serif;
  }
  .headline-soft {
    display: block;
    font-weight: 500;
    font-size: 86px;
    line-height: 92px;
    color: var(--ink);
  }
  .headline-strong {
    display: block;
    font-weight: 900;
    font-size: 92px;
    line-height: 100px;
    color: var(--navy);
    letter-spacing: -1px;
  }
  .headline-strong.first { margin-top: 8px; }
  .roof-icon {
    position: absolute;
    left: 876px;
    top: 160px;
  }
  .phone-icon {
    position: absolute;
    left: 120px;
    top: 608px;
  }
  .phone-number {
    position: absolute;
    left: 258px;
    top: 585px;
    font-family: "Roboto", sans-serif;
    font-weight: 900;
    font-size: 126px;
    line-height: 150px;
    color: var(--white);
    letter-spacing: -1px;
  }
  .website {
    position: absolute;
    left: 110px;
    width: 520px;
    top: 788px;
    text-align: center;
    font-family: "Roboto Slab", serif;
    font-weight: 700;
    font-size: 31px;
    color: var(--navy);
  }
  .address {
    position: absolute;
    left: 758px;
    top: 790px;
    font-family: "Roboto Slab", serif;
    font-weight: 500;
    font-size: 31px;
    line-height: 42px;
    color: var(--white);
  }
  .address-pin {
    position: absolute;
    left: 718px;
    top: 792px;
  }
</style>
</head>
<body>
  <main class="yard-sign">
    <svg class="sign-shapes" width="1200" height="900" viewBox="0 0 1200 900" aria-hidden="true">
      <rect class="top-band" x="0" y="0" width="1200" height="111" fill="var(--navy)"/>
      <polygon class="seal-tab" points="138,34 536,34 613,111 61,111" fill="var(--white)"/>
      <rect class="phone-band" x="0" y="590" width="1200" height="141" fill="var(--navy)"/>
      <rect class="footer-band" x="0" y="770" width="1200" height="130" fill="var(--charcoal)"/>
      <polygon class="website-tab" points="0,770 669,770 585,859 148,859 59,770" fill="var(--white)"/>
      <rect x="0" y="770" width="59" height="130" fill="var(--charcoal)"/>
      <circle class="seal-ring" cx="325" cy="308" r="236" fill="var(--white)" stroke="#bdbdc0" stroke-width="6"/>
      <circle cx="325" cy="308" r="222" fill="none" stroke="#2a2a2a" stroke-width="2"/>
    </svg>

    <div class="brand-seal">
      <div class="brand-name">DELVANE<br>ROOFING</div>
    </div>

    <div class="tagline-top">Family Owned Since 1956</div>

    <h1 class="headline" style="margin:0">
      <span class="headline-soft">Your</span>
      <span class="headline-soft">Hometown</span>
      <span class="headline-strong first">ROOFING</span>
      <span class="headline-strong">EXPERTS</span>
    </h1>

    <svg class="roof-icon" width="240" height="100" viewBox="0 0 240 100" aria-hidden="true">
      <polygon points="0,52 70,0 110,0 240,95 195,95 90,18 14,52" fill="#2f2f31"/>
      <polygon points="90,18 195,95 150,95 85,46" fill="#2f2f31" opacity="0"/>
      <line x1="118" y1="20" x2="148" y2="20" stroke="#f0f0f1" stroke-width="3"/>
      <line x1="140" y1="44" x2="172" y2="44" stroke="#f0f0f1" stroke-width="3"/>
      <line x1="168" y1="68" x2="202" y2="68" stroke="#f0f0f1" stroke-width="3"/>
      <rect x="48" y="66" width="11" height="11" fill="#2f2f31"/>
      <rect x="62" y="66" width="11" height="11" fill="#2f2f31"/>
      <rect x="48" y="80" width="11" height="11" fill="#2f2f31"/>
      <rect x="62" y="80" width="11" height="11" fill="#2f2f31"/>
    </svg>

    <svg class="phone-icon" width="110" height="110" viewBox="0 0 110 110" aria-hidden="true">
      <path d="M22 14 L38 12 L48 36 L38 44 C44 60 54 70 68 76 L76 66 L100 76 L98 92 C96 100 88 104 78 102 C46 94 18 66 10 34 C8 24 12 16 22 14 Z" fill="none" stroke="var(--white)" stroke-width="5" stroke-linejoin="round"/>
      <path d="M60 30 A22 22 0 0 1 80 50" fill="none" stroke="var(--white)" stroke-width="5" stroke-linecap="round"/>
      <path d="M62 16 A36 36 0 0 1 94 48" fill="none" stroke="var(--white)" stroke-width="5" stroke-linecap="round"/>
      <path d="M64 2 A50 50 0 0 1 108 46" fill="none" stroke="var(--white)" stroke-width="5" stroke-linecap="round"/>
    </svg>
    <div class="phone-number">337-555-0148</div>

    <div class="website">www.delvaneroofing.com</div>

    <svg class="address-pin" width="24" height="30" viewBox="0 0 24 30" aria-hidden="true">
      <path d="M12 2 C6 2 2 6.5 2 12 C2 19 12 28 12 28 C12 28 22 19 22 12 C22 6.5 18 2 12 2 Z" fill="none" stroke="var(--white)" stroke-width="2"/>
      <circle cx="12" cy="12" r="3.5" fill="none" stroke="var(--white)" stroke-width="2"/>
    </svg>
    <div class="address">468 Pettigrew Rd,<br>Lake Charles LA 70452</div>
  </main>
</body>
</html>
```